Australian IT Company New Logo Business Cards Required

We are a computer consultancy / MSP located in Brisbane Australia looking to have business cards designed with our new logo, we are looking for something professional that catches the eye.
I can provide the logo in other formats if required, let's see what you can create!

```html
<!DOCTYPE html>
<html lang="en">
<head>
<meta charset="utf-8">
<title>Corvelo Business Cards</title>
<link href="https://fonts.googleapis.com/css2?family=Lato:wght@400;700;900&display=swap" rel="stylesheet">
<style>
  :root {
    --brand-green: #8ac543;
    --ink-grey: #6f6f6f;
    --swoosh-grey: #8a8a8a;
    --paper: #ffffff;
    --backdrop: #3a3b3e;
  }
  html, body {
    margin: 0;
    padding: 0;
    width: 1200px;
    height: 900px;
    overflow: hidden;
    background: var(--backdrop);
    font-family: 'Lato', sans-serif;
  }
  .canvas {
    width: 1200px;
    height: 900px;
    display: flex;
    flex-direction: column;
    align-items: center;
    justify-content: center;
    gap: 56px;
  }
  .card {
    position: relative;
    width: 620px;
    height: 354px;
    border-radius: 26px;
    overflow: hidden;
    box-shadow: 0 14px 30px rgba(0,0,0,0.35);
  }
  .card--front {
    background: var(--brand-green);
    display: flex;
    align-items: center;
    justify-content: center;
  }
  .card--back { background: var(--paper); }

  .brand { display: flex; flex-direction: column; }
  .brand__name {
    font-weight: 900;
    font-size: 62px;
    letter-spacing: 2px;
    line-height: 1;
    text-transform: uppercase;
  }
  .brand__tagline {
    font-weight: 700;
    font-size: 15px;
    letter-spacing: 2.4px;
    text-transform: uppercase;
    margin-top: 6px;
  }
  .card--front .brand { color: var(--paper); align-items: center; }

  .card--back .brand {
    position: absolute;
    left: 50px;
    top: 120px;
  }
  .card--back .brand__name { color: var(--brand-green); font-size: 48px; }
  .card--back .brand__tagline { color: var(--ink-grey); font-size: 12px; letter-spacing: 2px; }

  .wave {
    position: absolute;
    inset: 0;
    width: 100%;
    height: 100%;
  }
  .person {
    position: absolute;
    right: 40px;
    top: 36px;
    text-align: right;
  }
  .person__name {
    color: var(--brand-green);
    font-weight: 900;
    font-size: 30px;
    letter-spacing: 0.5px;
    margin: 0;
  }
  .person__role {
    color: var(--ink-grey);
    font-size: 16px;
    margin: 2px 0 0;
  }
  .contact {
    position: absolute;
    right: 30px;
    top: 205px;
    text-align: right;
    color: var(--paper);
    font-size: 14px;
    line-height: 1.42;
    margin: 0;
    font-style: normal;
  }
</style>
</head>
<body>
<main class="canvas">
  <section class="card card--front">
    <div class="brand">
      <span class="brand__name">Corvelo</span>
      <span class="brand__tagline">IT Solutions for Small Business</span>
    </div>
  </section>

  <section class="card card--back">
    <svg class="wave" viewBox="0 0 620 354" aria-hidden="true">
      <path d="M620,110 C500,118 440,150 400,200 C360,260 300,320 180,354 L620,354 Z" fill="var(--brand-green)"/>
      <path d="M596,104 C484,112 424,146 382,198 C342,256 282,318 168,350" fill="none" stroke="var(--brand-green)" stroke-width="5"/>
      <path d="M120,322 C240,316 320,292 352,232 C342,288 280,330 130,338 Z" fill="var(--swoosh-grey)"/>
      <path d="M100,354 C200,346 260,342 300,330 L300,354 Z" fill="var(--brand-green)"/>
    </svg>

    <div class="brand">
      <span class="brand__name">Corvelo</span>
      <span class="brand__tagline">IT Solutions for Small Business</span>
    </div>

    <div class="person">
      <p class="person__name">JOHN SMITH</p>
      <p class="person__role">Founder &amp; CEO</p>
    </div>

    <address class="contact">
      1234 First Line Address<br>
      5678 Second Line Address<br>
      1234567890<br>
      info@yourmail.com<br>
      www.yourwebsite.com
    </address>
  </section>
</main>
</body>
</html>
```